Flaschenetikett Jörgi`s ColaMix
Zielgruppe
Wir machen einen ColaMix, weil wir es können und ihm eine Prise 80er verpassen wollen.
Hip, Trendig und ein bisschen Oldschool.
Bei uns kommt nur in die Flasche, was uns selber schmeckt und dabei preislich fair ist! Kein Schnickschnack, dafür mit viel Geschmack und einer Portion Oldschool.
Einfach einen richtig guten Brauso ähhmm, ColaMix!
Farben:
orange / weiss (Hintergrund Orange & Schrift Weiss)
oder
weiss / anthrazit
Flaschenfarbe:
braun
Etikettgröße:
max. 10 x 10 cm
Name:
Jörgis ColaMix
Zusatztext:
MÜNCHEN
ColaMix (muss irgendwo auf dem Etikett stehen)
Die Beispiele finden wir ultra hip, ein bisschen oldschool, trendig und genau richtig. Alles simpel, kein BlimBlim aber dafür einen ziemlich hohen Stylfaktor.
Wir sind nicht modern, sondern Kinder der 80iger, stehen auf Industrie Vintage Zeug und brauchen einen "ColaMix" der zu uns passt.
Jörg, ja einfach Jörg soll er heissen. Ein deutscher Trendname aus dem 19.Jahrhundert und doch jung und frisch! Genau wie unser ColaMix.
Das Kultgetränk das Allen schmeckt kommt in einer Oldschool braunen Flasche um die Ecke.
WIR MACHEN UNS FAST IN DIE HOSEN VOR AUFREGUNG, WAS IHR SO AUF DER FLASCHE HABT!!!!
HAUT REIN!!!

```html
<!DOCTYPE html>
<html lang="de">
<head>
<meta charset="utf-8">
<title>Jörgi's ColaMix – Flaschenetikett</title>
<link rel="stylesheet" href="https://fonts.googleapis.com/css2?family=Yesteryear&family=Lobster&family=Signika:wght@600&family=Roboto+Slab:wght@700&display=swap">
<style>
  :root {
    --orange: #ee8540;
    --orange-soft: #f3a36c;
    --orange-tint: #fadcc6;
    --white: #ffffff;
    --stage: #ececec;
    --label-size: 400px;
  }
  * { box-sizing: border-box; margin: 0; padding: 0; }
  html, body {
    width: 1200px;
    height: 857px;
    overflow: hidden;
    background: var(--stage);
  }
  .stage {
    width: 1200px;
    height: 857px;
    display: flex;
    justify-content: center;
    align-items: center;
    gap: 60px;
  }
  .label {
    position: relative;
    width: var(--label-size);
    height: var(--label-size);
    overflow: hidden;
    box-shadow: 0 3px 10px rgba(0,0,0,0.18);
  }
  .label--orange { background: var(--orange); color: var(--white); }
  .label--white  { background: var(--white);  color: var(--orange); }

  .label__band {
    position: absolute;
    left: 0;
    width: 100%;
    height: 8px;
    background: currentColor;
  }
  .label__band--top { top: 48px; }
  .label__band--bottom { top: 320px; }

  .label__burst {
    position: absolute;
    left: 20px;
    width: 360px;
    height: 38px;
  }
  .label__burst--top { top: 6px; }
  .label__burst--bottom { top: 332px; }
  .label--orange .label__burst {
    background: radial-gradient(ellipse at center, var(--orange-soft) 0%, var(--orange) 75%);
  }
  .label--white .label__burst {
    background: radial-gradient(ellipse at center, var(--orange-tint) 0%, var(--white) 75%);
  }

  .label__text {
    position: absolute;
    left: 0;
    width: 100%;
    text-align: center;
    line-height: 1;
    white-space: nowrap;
  }
  .label__name {
    top: 56px;
    font-family: "Yesteryear", cursive;
    font-weight: 400;
    font-size: 128px;
  }
  .label__product {
    top: 180px;
    font-family: "Lobster", cursive;
    font-size: 102px;
  }
  .label--white .label__name { top: 58px; font-size: 122px; }
  .label--white .label__product { top: 186px; font-size: 80px; }

  .label__since {
    top: 288px;
    font-family: "Lobster", cursive;
    font-size: 19px;
  }
  .label__since--caps {
    top: 289px;
    font-family: "Signika", sans-serif;
    font-weight: 600;
    font-size: 19px;
    letter-spacing: 0.06em;
    word-spacing: 0.3em;
  }
  .label__original {
    top: 265px;
    left: auto;
    right: 52px;
    width: auto;
    font-family: "Roboto Slab", serif;
    font-weight: 700;
    font-size: 10px;
    letter-spacing: 0.08em;
  }
  .label__city {
    top: 373px;
    font-family: "Lobster", cursive;
    font-size: 19px;
  }
</style>
</head>
<body>
<main class="stage">

  <section class="label label--orange" aria-label="Etikett Orange mit weißer Schrift">
    <div class="label__burst label__burst--top" role="img" aria-label="Strahlenkranz-Ornament in Weiß"></div>
    <div class="label__band label__band--top"></div>
    <h1 class="label__text label__name">Jörgi's</h1>
    <p class="label__text label__product">Cola Mix</p>
    <p class="label__text label__since">since 2016</p>
    <div class="label__band label__band--bottom"></div>
    <div class="label__burst label__burst--bottom" role="img" aria-label="Strahlenkranz-Ornament in Weiß"></div>
    <p class="label__text label__city">Made for MUNICH</p>
  </section>

  <section class="label label--white" aria-label="Etikett Weiß mit oranger Schrift">
    <div class="label__burst label__burst--top" role="img" aria-label="Strahlenkranz-Ornament in Orange"></div>
    <div class="label__band label__band--top"></div>
    <h2 class="label__text label__name">Jörgi's</h2>
    <p class="label__text label__product">Cola Mix</p>
    <p class="label__text label__original">ORIGINAL</p>
    <p class="label__text label__since--caps">SINCE 2016</p>
    <div class="label__band label__band--bottom"></div>
    <div class="label__burst label__burst--bottom" role="img" aria-label="Strahlenkranz-Ornament in Orange"></div>
    <p class="label__text label__city">Made for MUNICH</p>
  </section>

</main>
</body>
</html>
```